依頼詳細
宮城県仙台市太白区に新たにオープンするサロンのチラシの依頼になります。
近くにはNOVRAや大きい公園など緑もあり綺麗な街並みの中ある
ナチュラルだけどスタイリッシュさもあり柔らかいイメージのサロン内装にしようと思っております。
女性的柔らかいおしゃれなデザインを希望しております。
またまつげサロン併設店で同時オープン。
記載項目
宮城県仙台市太白区緑丘2-7-4 さくらんぼテラスモール
T.O.V by verdalis 緑丘店
℡OOOーOOOーOOOO
Quinvara eyelash
℡OOOーOOOーOOO
2023.8.O NEW OPEN

このチラシ持参でトリートメントプレゼント

(電話番号、オープン日まだ確定してないので調整かけたい)
(QRコードを美容室、まつげサロン用に2箇所)

近隣マップ

サイズ
A5
ページ数
両面
希望イメージ
シンプル 複雑
単色 カラフル
暗い 明るい
日常 高級
遊び心 厳粛
未来的 伝統的
女性的 男性的
希望する色
赤系、青系、水色系、緑系、黄・オレンジ系、グレー系、紫系
納品ファイル
• 高解像度JPG (.jpg)
• イラストレーター形式 (.ai)
• フォトショップ形式 (.psd)
補足説明
店内写真は必ず入れたい。
まだ写真がないから
パースを入れてほしい。
差し替えできるようにしてほしい
両目でお願いしたい。
裏面に料金
表面スタイル写真は一つで
あまりガチャつかないでおしゃれさとわかりやすさ、見やすさがほしいです。
■ 選んだ理由

夏っぽくかつ全体のバランスが良く素敵なデザインだと思った。

■ 提案者全員のお礼・コメント

この度は弊社のチラシデザインコンペに参加いただきまして誠にありがとうございました。
来年また出店がございますのでその際にコンペさせていただきますので
またのご参加お待ち致しております。

```html
<!DOCTYPE html>
<html lang="ja">
<head>
<meta charset="utf-8">
<title>T.O.V by verdalis / Quinvara eyelash 料金表</title>
<link href="https://fonts.googleapis.com/css2?family=Cormorant+Garamond:wght@500;600&family=Great+Vibes&family=Noto+Sans+JP:wght@400;500;700&display=swap" rel="stylesheet">
<style>
:root{
  --ink:#4a4548;
  --ink-soft:#6d676a;
  --accent:#e2647f;
  --panel-top:#f7e3e4;
  --panel-bottom:#fbeeee;
  --paper:#ffffff;
  --script:#f1cfd4;
}
*{box-sizing:border-box;margin:0;padding:0}
html,body{width:846px;height:1200px;overflow:hidden;background:var(--paper)}
body{position:relative;font-family:"Noto Sans JP",sans-serif;color:var(--ink)}
.photo{position:absolute}
.photo--products{left:56px;top:28px;width:240px;height:198px;background:linear-gradient(120deg,#f3d7da 0%,#c8324a 45%,#e9b9bf 70%,#f6e6e7 100%)}
.photo--model-top{left:318px;top:28px;width:262px;height:198px;background:linear-gradient(135deg,#d8c2b4 0%,#8c6a58 50%,#e7d6cc 100%)}
.photo--style-1{left:598px;top:0;width:248px;height:296px;background:linear-gradient(160deg,#efe4de 0%,#d49aa6 55%,#f2e8e3 100%)}
.photo--style-2{left:598px;top:296px;width:248px;height:282px;background:linear-gradient(160deg,#b9c9d6 0%,#8a6d5b 50%,#e2d3c8 100%)}
.photo--style-3{left:598px;top:578px;width:248px;height:296px;background:linear-gradient(160deg,#f4efe9 0%,#c9a98d 50%,#ece3da 100%)}
.photo--style-4{left:598px;top:874px;width:248px;height:326px;background:linear-gradient(160deg,#ede8e4 0%,#7a6258 50%,#d9cdc5 100%)}
.photo--eye{left:403px;top:1075px;width:176px;height:70px;background:linear-gradient(90deg,#e6dfdc 0%,#8d817d 50%,#e6dfdc 100%)}

.feature{position:absolute;top:240px}
.feature--new{left:56px;width:250px}
.feature--recommend{left:318px;width:262px}
.feature__label{font-size:15px;font-weight:500;color:var(--ink)}
.feature__label::before{content:"●";color:var(--accent);margin-right:5px;font-size:11px;vertical-align:2px}
.feature__row{display:flex;justify-content:space-between;align-items:flex-end;margin-top:5px}
.feature__name{font-size:14px;line-height:1.45;font-weight:500}
.feature__price{font-size:28px;font-weight:700;color:var(--accent);letter-spacing:.5px;line-height:1}
.feature__text{font-size:10px;line-height:1.75;color:var(--ink-soft);margin-top:9px}

.salon{position:absolute;left:40px;top:408px;width:552px;height:468px;background:linear-gradient(180deg,var(--panel-top),var(--panel-bottom));padding:38px 22px 0 22px}
.script{position:absolute;font-family:"Great Vibes",cursive;color:var(--script);opacity:.75}
.salon .script{right:30px;top:10px;font-size:84px}
.salon__title{position:relative;font-family:"Cormorant Garamond",serif;font-weight:600;font-size:36px;letter-spacing:1px;color:var(--ink)}
.salon__title small{font-size:24px;font-weight:500}
.salon__note{position:relative;font-size:13px;font-weight:500;margin:16px 0 8px}
.salon__note::before{content:"●";color:var(--accent);margin-right:5px;font-size:10px;vertical-align:2px}
.price-list{position:relative;list-style:none}
.price-list li{display:flex;justify-content:space-between;font-size:13.5px;line-height:25.4px;font-weight:500}
.price-list em{font-style:normal;font-size:10px}

.lash{position:absolute;left:40px;top:876px;width:552px;height:324px}
.lash .script{right:30px;top:0;font-size:76px}
.lash__title{position:absolute;left:16px;top:12px;font-family:"Cormorant Garamond",serif;font-weight:600;font-size:36px;letter-spacing:.5px}
.lash__col{position:absolute;top:74px}
.lash__col--sable{left:16px;width:142px}
.lash__col--flat{left:186px;width:142px}
.lash__col--perm{left:363px;width:176px}
.lash__head{font-size:13px;font-weight:500;margin-bottom:6px}
.lash__head::before{content:"●";color:var(--accent);margin-right:4px;font-size:10px;vertical-align:2px}
.lash__list{list-style:none}
.lash__list li{display:flex;justify-content:space-between;font-size:14px;line-height:25px;font-weight:500}
.lash__product{font-size:11.5px;font-weight:500;line-height:1.5;letter-spacing:.5px;margin-top:4px}
.lash__price{font-size:15px;font-weight:500;text-align:right;margin-top:6px;padding-right:20px}
</style>
</head>
<body>
<div class="photo photo--products" role="img" aria-label="ヘアケア製品ボトルの写真"></div>
<div class="photo photo--model-top" role="img" aria-label="ロングヘアのスタイル写真"></div>
<div class="photo photo--style-1" role="img" aria-label="ピンクカラーのヘアスタイル写真"></div>
<div class="photo photo--style-2" role="img" aria-label="ショートボブのヘアスタイル写真"></div>
<div class="photo photo--style-3" role="img" aria-label="ベージュカラーのヘアスタイル写真"></div>
<div class="photo photo--style-4" role="img" aria-label="ダークトーンのヘアスタイル写真"></div>

<section class="feature feature--new">
  <p class="feature__label">New Menu</p>
  <div class="feature__row">
    <p class="feature__name">オルフェアトリートメント+<br>カット+カラー</p>
    <p class="feature__price">¥9,200</p>
  </div>
  <p class="feature__text">日本の女性の髪を研究して作られた最高峰トリートメント。一人一人の髪質や状態に合わせて、一番あった組み合わせをお選びします。</p>
</section>

<section class="feature feature--recommend">
  <p class="feature__label">Recommended Menu</p>
  <div class="feature__row">
    <p class="feature__name">ルミエナカラー+カット<br>（ロング料金なし）</p>
    <p class="feature__price">¥6,900</p>
  </div>
  <p class="feature__text">日本人特有の赤みを抑えて外国人のような透明感を出してくれる今話題のカラー。ツヤ感と柔らかさで、自然に透け感のあるグレージュ系ヘアに。</p>
</section>

<section class="salon">
  <span class="script" aria-hidden="true">Menu</span>
  <h2 class="salon__title">T.O.V <small>by verdalis</small></h2>
  <p class="salon__note">ロング料金なし</p>
  <ul class="price-list">
    <li><span>ドライカット</span><span>¥2,700</span></li>
    <li><span>カット+シャンプー</span><span>¥3,200</span></li>
    <li><span>カット+ハルモニトリートメント</span><span>¥4,400</span></li>
    <li><span>カット+リタッチカラー</span><span>¥4,500</span></li>
    <li><span>カット+全体カラー<em>（白髪染めも同料金）</em></span><span>¥5,500</span></li>
    <li><span>カット+ハルモニトリートメント</span><span>¥5,500</span></li>
    <li><span>カット+カラー+ハルモニトリートメント</span><span>¥6,900</span></li>
    <li><span>縮毛矯正+カット</span><span>¥7,900</span></li>
    <li><span>コールドパーマ+カット</span><span>¥7,900</span></li>
    <li><span>デジタルパーマ+カット</span><span>¥7,900</span></li>
    <li><span>縮毛矯正+カット+カラー</span><span>¥10,500</span></li>
    <li><span>デジタルパーマ+カット+カラー</span><span>¥10,500</span></li>
  </ul>
</section>

<section class="lash">
  <span class="script" aria-hidden="true">Menu</span>
  <h2 class="lash__title">Quinvara eyelash</h2>
  <div class="lash__col lash__col--sable">
    <p class="lash__head">Premium Sable</p>
    <ul class="lash__list">
      <li><span>60本</span><span>¥3,000</span></li>
      <li><span>80本</span><span>¥3,600</span></li>
      <li><span>100本</span><span>¥3,800</span></li>
      <li><span>120本</span><span>¥4,500</span></li>
      <li><span>140本</span><span>¥5,100</span></li>
    </ul>
  </div>
  <div class="lash__col lash__col--flat">
    <p class="lash__head">Flat Lash</p>
    <ul class="lash__list">
      <li><span>60本</span><span>¥4,100</span></li>
      <li><span>80本</span><span>¥4,600</span></li>
      <li><span>100本</span><span>¥5,000</span></li>
      <li><span>120本</span><span>¥5,600</span></li>
      <li><span>140本</span><span>¥6,100</span></li>
    </ul>
  </div>
  <div class="lash__col lash__col--perm">
    <p class="lash__head">まつ毛パーマ</p>
    <p class="lash__product">CÉLESTINE<br>LASHLIFT</p>
    <p class="lash__price">¥4,900</p>
  </div>
</section>
<div class="photo photo--eye" role="img" aria-label="まつ毛パーマ仕上がりの目元写真"></div>
</body>
</html>
```